Brochure Cover and Back pages

We are a US-based cosmetics company that sells state-of-the-art skin care products, including advanced anti-aging serums, natural mineral sunscreens, organic antioxidant moisturizers, and organic face cleansers. We need a product brochure. We already have chosen a design for the layout of the product info pages. But we still need a cover page and a back page. We are looking for simple but elegant design for the cover page. The back page is less important and we already know what we want on the back page. It will be the company's mission statement and at the bottom, the company URL, phone number, etc.

The brochure has two folds. So there will be three panels on both sides. The size of each panel is 16.5 (l) x 9.5 (w) cm.

At the end of the project, we expect the designer to integrate all the pages so that the finished copy is read to be sent off to a printing service for printing.

All the product info pages are attached. Also attached are the text (info) to go on the back page, company logo with and without the tagline, the icon in the logo.

YOu are welcome to visit our website www.morvask.com to learn about our products.

Industry/Entity Type

Cosmetics

```html
<!DOCTYPE html>
<html lang="en">
<head>
<meta charset="utf-8">
<title>Morvask Brochure – Back and Cover Panels</title>
<link rel="stylesheet" href="https://fonts.googleapis.com/css2?family=Tinos:wght@400;700&family=Source+Sans+3:wght@400;600&display=swap">
<style>
  :root {
    --brand-blue: #0093dd;
    --paper: #ffffff;
    --ink: #111111;
    --serif: "Tinos", "Times New Roman", serif;
    --sans: "Source Sans 3", "Myriad Pro", sans-serif;
  }
  * { margin: 0; padding: 0; box-sizing: border-box; }
  html, body { width: 1200px; height: 1042px; overflow: hidden; background: var(--paper); }
  .spread { position: relative; width: 1200px; height: 1042px; display: flex; }
  .panel { position: relative; height: 100%; }
  .panel--back { width: 594px; background: var(--brand-blue); color: var(--paper); }
  .panel--cover { width: 606px; background: var(--paper); color: var(--ink); }

  .wordmark {
    position: absolute; top: 190px; left: 0; width: 100%;
    text-align: center; font-family: var(--serif); font-weight: 400;
    font-size: 66px; letter-spacing: 1px; color: var(--ink);
  }
  .cover-title {
    position: absolute; top: 426px; left: 0; width: 100%;
    text-align: center; font-family: var(--serif); font-weight: 700;
    font-size: 38px; line-height: 52px; color: var(--brand-blue);
  }
  .title-rule { position: absolute; top: 550px; left: 172px; width: 250px; height: 8px; }

  .lead {
    position: absolute; top: 700px; left: 0; width: 100%;
    text-align: center; font-family: var(--sans); font-weight: 600;
    font-size: 22px; line-height: 29px;
  }
  .pill {
    position: absolute; top: 885px; width: 403px; height: 42px;
    border-radius: 10px; display: flex; align-items: center; justify-content: center;
    font-family: var(--serif); font-size: 21px; letter-spacing: 0.3px;
  }
  .panel--back .pill { left: 96px; background: var(--paper); color: var(--brand-blue); }
  .panel--cover .pill { left: 95px; background: var(--brand-blue); color: var(--paper); }
  .pill-note {
    position: absolute; top: 932px; left: 0; width: 100%;
    text-align: center; font-family: var(--sans); font-size: 18px;
  }
</style>
</head>
<body>
<main class="spread">
  <section class="panel panel--back">
    <p class="lead">Olumquis es invel inullant<br>laborer cipictotatur molorem</p>
    <div class="pill">ALIQUO VOLUPTAT. IC</div>
    <p class="pill-note">Ibearum rehenis es reperrum a dundit ut</p>
  </section>

  <section class="panel panel--cover">
    <div class="wordmark">Morvask</div>
    <h1 class="cover-title">Dolecustium Vel Milia<br>Ipid Utati Nis Ellibu</h1>
    <svg class="title-rule" viewBox="0 0 250 8" aria-hidden="true">
      <path d="M0 4 Q125 -1 250 4 Q125 9 0 4 Z" fill="var(--brand-blue)"/>
    </svg>
    <p class="lead">Inversperit ut auditis volupta<br>tempos dolorepro eosa</p>
    <div class="pill">NOS AUT EAQUO</div>
    <p class="pill-note">Qui Cum Voluptatem Sequat</p>
  </section>
</main>
</body>
</html>
```